Need a web design for my company which has an existing logo already

Hello,
I am looking for a web designer for my sports and well-being company. I've got a logo already which should be used for the creation. I will need the entire design idea for my word press website (5 -10 pages) .
Please see the attached logo.
My company is a yoga, dance and retreat business, but not only for women. So it shouldn't be girly. I am looking for a neutral design.
I am looking forward to read your proposals. Please show me some samples of similar jobs you have done in the past.
best regards,
Tova

```html
<!DOCTYPE html>
<html lang="en">
<head>
<meta charset="utf-8">
<title>Lumen Studio</title>
<link href="https://fonts.googleapis.com/css2?family=IBM+Plex+Sans:wght@400;500;600;700&family=Parisienne&display=swap" rel="stylesheet">
<style>
:root{
  --ink:#1d1d1f;
  --text:#333;
  --white:#fff;
  --footer:#231f20;
  --soft:#f3f1f0;
  --social:#2f5fb0;
  --line:#e4e1df;
}
*{margin:0;padding:0;box-sizing:border-box}
html,body{width:1200px;height:3850px;overflow:hidden}
body{font-family:"IBM Plex Sans",Arial,sans-serif;color:var(--text);background:var(--white);position:relative}
.abs{position:absolute}
.script{font-family:"Parisienne",cursive;font-weight:400}
.btn{position:absolute;border:2px solid var(--ink);background:transparent;color:var(--ink);font-weight:700;font-size:12px;letter-spacing:.2px;display:flex;align-items:center;justify-content:center;text-transform:uppercase}
.btn-lg{font-size:14px}
.title{position:absolute;left:0;width:1200px;text-align:center;font-weight:600;font-size:24px;color:var(--ink);letter-spacing:.3px}
.title::after{content:"";display:block;width:40px;height:3px;background:var(--ink);margin:14px auto 0}

/* hero */
.hero{position:absolute;left:0;top:0;width:1200px;height:672px;background:linear-gradient(180deg,#4f86ad 0%,#8fb2c9 28%,#9fb6c0 48%,#6f8c93 68%,#4b5046 86%,#3b3428 100%)}
.brand{position:absolute;left:130px;top:30px;color:var(--white);font-size:44px;font-weight:500;line-height:1}
.brand small{display:block;font-size:13px;letter-spacing:8px;margin:6px 0 0 64px}
.follow{position:absolute;left:704px;top:28px;display:flex;align-items:center;gap:10px;color:var(--ink);font-size:12px}
.dot-icon{width:24px;height:24px;border-radius:50%;background:var(--social)}
.call{position:absolute;left:946px;top:20px;border-left:1px solid rgba(255,255,255,.7);padding-left:18px;color:var(--white)}
.call span{display:block;font-size:12px}
.call strong{display:block;font-size:20px;font-weight:600;margin-top:4px;text-decoration:underline}
.phone-ico{position:absolute;left:908px;top:28px}
.nav{position:absolute;top:83px;left:0;width:1200px;font-size:14px;color:var(--ink)}
.nav a{position:absolute;color:var(--ink);text-decoration:none}
.welcome{position:absolute;left:675px;top:205px;color:var(--ink)}
.welcome .w1{font-size:40px;line-height:1}
.welcome .w2{font-size:64px;line-height:1.1}
.dots{position:absolute;top:617px;left:562px;display:flex;gap:10px;align-items:center}
.dots i{width:6px;height:6px;border-radius:50%;background:var(--white)}
.dots i.on{width:11px;height:11px;background:transparent;border:2px solid var(--white)}

/* services */
.card{position:absolute;background:var(--white);box-shadow:0 2px 8px rgba(0,0,0,.12)}
.card .ph{height:185px}
.card h3{font-size:30px;color:var(--ink);margin:24px 0 0 26px}
.card p{font-size:13.5px;line-height:19px;margin:12px 26px 0 26px;color:var(--text)}

/* about */
.about{position:absolute;left:0;top:1258px;width:1200px;height:584px;background:linear-gradient(180deg,#f7f0ee 0%,#f4e9e4 55%,#e7d3c6 80%,#8e8a88 100%)}
.about p{position:absolute;left:262px;width:676px;top:110px;text-align:center;font-size:16.5px;line-height:22.5px;color:var(--text)}

/* feature */
.feature-box{position:absolute;left:563px;top:2021px;width:496px;height:410px;background:var(--white)}
.feature-box h2{position:absolute;left:40px;top:36px;font-size:24px;font-weight:600;line-height:36px;color:var(--ink)}
.feature-box .rule{position:absolute;left:40px;top:118px;width:40px;height:3px;background:var(--ink)}
.feature-box p{position:absolute;left:40px;top:152px;width:390px;font-size:16.5px;line-height:24px}

/* testimonials */
.testi{position:absolute;left:0;top:2481px;width:1200px;height:440px;background:linear-gradient(180deg,#3a3939 0%,#2f2e2e 50%,#272524 100%)}
.testi .title{color:var(--white);top:54px}
.testi .title::after{background:var(--white)}
.quote{position:absolute;left:250px;width:700px;top:148px;text-align:center;color:var(--white);font-size:17.5px;line-height:26px}
.qmark{position:absolute;color:var(--white);font-size:44px;font-weight:700;font-family:Georgia,serif;line-height:1}
.avatar{position:absolute;left:572px;top:308px;width:54px;height:54px;border-radius:50%;background:#b9a48f}
.who{position:absolute;left:0;width:1200px;top:370px;text-align:center;color:var(--white);font-size:12.5px}

/* blog */
.blog{position:absolute;left:0;top:2921px;width:1200px;height:572px;background:var(--soft)}
.post{position:absolute;top:122px;width:302px;height:405px;background:var(--white);border:1px solid var(--line)}
.post .ph{height:192px}
.post h4{font-size:13.5px;font-weight:600;line-height:24px;color:var(--ink);margin:20px 24px 0}
.post p{font-size:11.5px;line-height:16.5px;margin:16px 24px 0}

/* footer */
.footer{position:absolute;left:0;top:3493px;width:1200px;height:357px;background:var(--footer);color:var(--white)}
.footer .brand{left:135px;top:82px}
.fcol{position:absolute;top:56px}
.fcol h5{font-size:13px;font-weight:700;letter-spacing:.5px;margin-bottom:18px}
.fcol li{list-style:none;font-size:11.5px;line-height:20px}
.fitem{display:flex;gap:12px;align-items:flex-start;margin-bottom:18px;font-size:11.5px;line-height:15px}
.fitem .c{width:24px;height:24px;border-radius:50%;background:var(--white);flex:none;display:flex;align-items:center;justify-content:center;margin-top:2px}
.fbar{position:absolute;left:130px;width:940px;top:266px;height:1px;background:#3c3839}
.fbottom{position:absolute;top:310px;font-size:11px}
</style>
</head>
<body>

<header class="hero" role="img" aria-label="Photo of a woman holding a standing yoga pose on a rock above misty mountains"></header>
<div class="brand">lumen<small>STUDIO</small></div>
<div class="follow">FOLLOW US <span class="dot-icon"></span><span class="dot-icon"></span><span class="dot-icon"></span></div>
<svg class="phone-ico" width="26" height="26" viewBox="0 0 24 24" fill="none" stroke="#fff" stroke-width="1.6"><path d="M5 3h4l2 5-2.5 1.5a11 11 0 0 0 6 6L16 13l5 2v4a2 2 0 0 1-2 2A17 17 0 0 1 3 5a2 2 0 0 1 2-2z"/></svg>
<div class="call"><span>CALL US NOW</span><strong>555.014.2290</strong></div>
<nav class="nav">
  <a style="left:487px">HOME</a><a style="left:565px">ABOUT US</a><a style="left:674px">SERVICES</a><a style="left:777px">TESTIMONIALS</a><a style="left:908px">BLOG</a><a style="left:983px">CONTACT US</a>
</nav>
<div class="welcome">
  <div class="w1 script">Welcome to</div>
  <div class="w2 script">Lumen Studio</div>
</div>
<a class="btn btn-lg" style="left:677px;top:342px;width:117px;height:42px">Read More</a>
<div class="dots"><i></i><i></i><i class="on"></i><i></i><i></i></div>

<section>
  <h2 class="title" style="top:712px">OUR SERVICES</h2>
  <article class="card" style="left:128px;top:792px;width:304px;height:415px">
    <div class="ph" role="img" aria-label="Photo of a woman in a backbend yoga pose in a bright white studio" style="background:linear-gradient(180deg,#e9e9e9,#cfcfcf)"></div>
    <h3 class="script">Yoga</h3>
    <p>Lorem ipsum dolor sit amet, consec tetur adipiscing elit, sed do eiusmod tempor incididunt ut labore . Ut enim ad minim veniam, quis nostrud</p>
    <a class="btn" style="left:30px;top:357px;width:89px;height:31px">Read More</a>
  </article>
  <article class="card" style="left:445px;top:792px;width:304px;height:415px">
    <div class="ph" role="img" aria-label="Photo of two dancers in bright colourful clothes against a red background" style="background:linear-gradient(180deg,#d8323c,#c9302f 60%,#e79a3c)"></div>
    <h3 class="script">Dance</h3>
    <p>Lorem ipsum dolor sit amet, consec tetur adipiscing elit, sed do eiusmod tempor incididunt ut labore . Ut enim ad minim veniam, quis nostrud</p>
    <a class="btn" style="left:30px;top:357px;width:89px;height:31px">Read More</a>
  </article>
  <article class="card" style="left:762px;top:792px;width:305px;height:415px">
    <div class="ph" role="img" aria-label="Photo of a person working on a laptop in a beach chair at sunset" style="background:linear-gradient(180deg,#7d6fa3,#e8916a 55%,#3b2d33)"></div>
    <h3 class="script">Retreat Business.</h3>
    <p>Lorem ipsum dolor sit amet, consec tetur adipiscing elit, sed do eiusmod tempor incididunt ut labore . Ut enim ad minim veniam, quis nostrud</p>
    <a class="btn" style="left:30px;top:357px;width:89px;height:31px">Read More</a>
  </article>
</section>

<section class="about" role="img" aria-label="Photo of a man seen from behind with arms stretched wide over a hazy mountain sunset">
  <h2 class="title" style="top:42px">ABOUT US</h2>
  <p>Sed ut perspiciatis unde omnis iste natus error sit voluptatem accusantium doloremque laudantium, totam rem aperiam, eaque ipsa quae ab illo inventore veritatis et quasi architecto beatae vitae dicta sunt explicabo. Nemo enim ipsam voluptatem quia voluptas sit aspernatur aut odit aut fugit, sed quia consequuntur magni dolores.</p>
  <a class="btn" style="left:549px;top:226px;width:103px;height:35px">Read More</a>
</section>

<section>
  <div class="abs" role="img" aria-label="Photo of a businessman cheering on a cloud with a laptop under a blue sky" style="left:130px;top:1882px;width:542px;height:549px;background:linear-gradient(160deg,#3a5a95,#4f6fa6 60%,#7f93bd)"></div>
  <div class="feature-box">
    <h2>SED UT PERSPICIATIS UNDE OMNIS<br>ISTE NATUS ERROR SIT.</h2>
    <div class="rule"></div>
    <p>Sed ut perspiciatis unde omnis iste natus error sit voluptatem accusantium doloremque laudantium, totam rem aperiam, eaque ipsa quae ab illo inventore veritatis et quasi architecto beatae vitae dicta sunt explicabo doloremque laudantium, totam rem aperiam, eaque ipsa quae ab illo inventore veritatis</p>
    <a class="btn" style="left:42px;top:354px;width:103px;height:37px">Read More</a>
  </div>
</section>

<section class="testi" role="img" aria-label="Dim photo of a woman stretching on a jetty by a lake">
  <h2 class="title">TESTIMONIALS</h2>
  <span class="qmark" style="left:270px;top:130px">&ldquo;</span>
  <p class="quote">Sed ut perspiciatis unde omnis iste natus error sit voluptatem accusantium doloremque laudantium, totam rem aperiam, eaque ipsa quae ab illo inventore veritatis et quasi architecto beatae vitae dicta sunt explicabo doloremque laudantium, totam rem aperiam, eaque ipsa quae ab illo inventore veritatis&nbsp; enim ipsam voluptatem quia voluptas sit aspernatur aut odit aut fugit, sed quia consequuntur</p>
  <span class="qmark" style="left:866px;top:256px">&rdquo;</span>
  <svg class="abs" style="left:128px;top:196px" width="18" height="28" viewBox="0 0 18 28"><path d="M14 3 4 14l10 11" fill="none" stroke="#fff" stroke-width="2.5"/></svg>
  <svg class="abs" style="left:1050px;top:196px" width="18" height="28" viewBox="0 0 18 28"><path d="m4 3 10 11L4 25" fill="none" stroke="#fff" stroke-width="2.5"/></svg>
  <div class="avatar" role="img" aria-label="Portrait photo of the client"></div>
  <div class="who">MARCUS</div>
</section>

<section class="blog">
  <h2 class="title" style="top:40px">LATEST BLOG</h2>
  <article class="post" style="left:130px">
    <div class="ph" role="img" aria-label="Photo of a smiling man on the phone at a desk with a laptop" style="background:linear-gradient(180deg,#8a8f92,#5f5a55)"></div>
    <h4>SED UT PERSPICIATIS UNDE OMNIS ISTE NATUS ERROR SIT VOLU</h4>
    <p>Nemo enim ipsam voluptatem quia voluptas sit aspernatur aut odit aut fugit, sed quia consequuntur.</p>
    <a class="btn" style="left:27px;top:346px;width:84px;height:30px;font-size:11px">Read More</a>
  </article>
  <article class="post" style="left:448px">
    <div class="ph" role="img" aria-label="Photo of a woman meditating with raised arms before mountains at dusk" style="background:linear-gradient(180deg,#b39886,#7a6458 60%,#3a2f2c)"></div>
    <h4>SED UT PERSPICIATIS UNDE OMNIS ISTE NATUS ERROR SIT VOLU</h4>
    <p>Nemo enim ipsam voluptatem quia voluptas sit aspernatur aut odit aut fugit, sed quia consequuntur.</p>
    <a class="btn" style="left:27px;top:346px;width:84px;height:30px;font-size:11px">Read More</a>
  </article>
  <article class="post" style="left:765px">
    <div class="ph" role="img" aria-label="Photo of a woman in a warrior yoga pose in a bright minimal room" style="background:linear-gradient(180deg,#d9d3cc,#b5aca3)"></div>
    <h4>SED UT PERSPICIATIS UNDE OMNIS ISTE NATUS ERROR SIT VOLU</h4>
    <p>Nemo enim ipsam voluptatem quia voluptas sit aspernatur aut odit aut fugit, sed quia consequuntur.</p>
    <a class="btn" style="left:27px;top:346px;width:84px;height:30px;font-size:11px">Read More</a>
  </article>
</section>

<footer class="footer">
  <div class="brand">lumen<small>STUDIO</small></div>
  <div class="fcol" style="left:470px">
    <h5>MENU</h5>
    <ul><li>HOME</li><li>ABOUT US</li><li>SERVICES</li><li>TESTIMONIALS</li><li>BLOG</li><li>CONTACT US</li></ul>
  </div>
  <div class="fcol" style="left:668px">
    <h5>CONTACT US</h5>
    <div class="fitem"><span class="c"><svg width="12" height="12" viewBox="0 0 24 24"><path d="M12 2a7 7 0 0 0-7 7c0 5 7 13 7 13s7-8 7-13a7 7 0 0 0-7-7zm0 9.5A2.5 2.5 0 1 1 12 6a2.5 2.5 0 0 1 0 5.5z" fill="#231f20"/></svg></span><div>2200 Alder Row<br>Fairview, CA 90000</div></div>
    <div class="fitem"><span class="c"><svg width="12" height="12" viewBox="0 0 24 24"><path d="M5 3h4l2 5-2.5 1.5a11 11 0 0 0 6 6L16 13l5 2v4a2 2 0 0 1-2 2A17 17 0 0 1 3 5a2 2 0 0 1 2-2z" fill="#231f20"/></svg></span><div>Call Us<br>555.014.2290</div></div>
    <div class="fitem"><span class="c"><svg width="12" height="12" viewBox="0 0 24 24"><path d="M3 6h18v12H3z" fill="#231f20"/><path d="m3 6 9 7 9-7" fill="none" stroke="#fff" stroke-width="1.5"/></svg></span><div>E mail Us<br>hello@lumenstudio.com</div></div>
  </div>
  <div class="fcol" style="left:958px">
    <h5>FOLLOW US</h5>
    <div class="fitem"><span class="c"></span><div>Like us on<br>PAGEFEED</div></div>
    <div class="fitem"><span class="c"></span><div>Follow us on<br>CHIRPER</div></div>
    <div class="fitem"><span class="c"></span><div>Follow us on<br>WORKNET</div></div>
  </div>
  <div class="fbar"></div>
  <div class="fbottom" style="left:135px">LOGIN | REGISTER | PRIVACY POLICY | TERMS &amp; CONDITIONS</div>
  <div class="fbottom" style="right:132px">Copyright © 2021 All Rights Reserved</div>
</footer>

</body>
</html>
```